Signage for a store*

logo on the two sides of the sign
in the middle is the name of the store witch is VORELT
at the bottom of the two logos, one side for location/address and the other side is contact details phone number is 718-392-6107 address is 2974 THE SIGN WILL BEE 15 FEET BY 4 FEET I WOULD LIKE THAT THE
BACKGROUND OF THE SIGN SHOULD HAVE A NICE COLOR BASE
THAT GOES FOR A WINE STORE

```html
<!DOCTYPE html>
<html lang="en">
<head>
<meta charset="UTF-8">
<title>VORELT Storefront Sign</title>
<link href="https://fonts.googleapis.com/css2?family=Zilla+Slab:wght@400&family=Playfair+Display:wght@400&display=swap" rel="stylesheet">
<style>
  :root {
    --backdrop: #e6e0dc;
    --sign-face: #0b0b0b;
    --sign-face-top: #1a1a1a;
    --sign-frame: #2a2e3c;
    --gold: #c9962e;
    --gold-light: #dcaa3c;
    --wine: #b0214f;
  }
  * { margin: 0; padding: 0; box-sizing: border-box; }
  html, body {
    width: 1200px;
    height: 800px;
    overflow: hidden;
    background: var(--backdrop);
  }
  .canvas {
    position: relative;
    width: 1200px;
    height: 800px;
    display: flex;
    align-items: center;
    justify-content: center;
  }
  .sign {
    position: relative;
    width: 1120px;
    height: 320px;
    border: 8px solid var(--sign-frame);
    background: linear-gradient(180deg, var(--sign-face-top) 0%, var(--sign-face-top) 40%, var(--sign-face) 52%, var(--sign-face) 100%);
  }
  .sign__name {
    position: absolute;
    left: 50%;
    top: 118px;
    transform: translateX(-50%);
    font-family: "Zilla Slab", serif;
    font-weight: 400;
    font-size: 122px;
    line-height: 1;
    letter-spacing: 4px;
    color: var(--gold);
    background: linear-gradient(180deg, var(--gold-light), var(--gold));
    -webkit-background-clip: text;
    background-clip: text;
    -webkit-text-fill-color: transparent;
  }
  .sign__side {
    position: absolute;
    top: 86px;
    width: 160px;
    display: flex;
    flex-direction: column;
    align-items: center;
  }
  .sign__side--left { left: 42px; }
  .sign__side--right { right: 42px; }
  .brand-mark {
    display: flex;
    flex-direction: column;
    align-items: center;
    gap: 8px;
    height: 104px;
    justify-content: center;
  }
  .brand-mark__dot {
    width: 18px;
    height: 18px;
    border-radius: 50%;
    background: var(--wine);
  }
  .brand-mark__name {
    font-family: "Zilla Slab", serif;
    font-weight: 400;
    font-size: 21px;
    letter-spacing: 1px;
    color: var(--wine);
  }
  .sign__detail {
    margin-top: 24px;
    font-family: "Playfair Display", serif;
    font-size: 13px;
    letter-spacing: 1.5px;
    color: var(--gold);
  }
</style>
</head>
<body>
  <main class="canvas">
    <section class="sign" aria-label="VORELT store sign">
      <div class="sign__side sign__side--left">
        <div class="brand-mark">
          <span class="brand-mark__dot"></span>
          <span class="brand-mark__name">VORELT</span>
        </div>
        <p class="sign__detail">2974</p>
      </div>

      <h1 class="sign__name">VORELT</h1>

      <div class="sign__side sign__side--right">
        <div class="brand-mark">
          <span class="brand-mark__dot"></span>
          <span class="brand-mark__name">VORELT</span>
        </div>
        <p class="sign__detail">718-392-6107</p>
      </div>
    </section>
  </main>
</body>
</html>
```